Business Card Design

I need business cards designed for a new company i have started that makes cakes, particularly themed kids cakes with a really modern design and I would like to have my business cards reflect this. I have attached some photos of cakes I have made and would like some to be used.

Industry/Entity Type

Business

Contact Information for Business Card

Business Name: Treats and Bakes by Marla
Mobile: 0427 918 053
email: marla@treatsandbakesbymarla.com.au
Instagram: instagram.com/treatsandbakesbymarla/
Facebook: fb.me/treatsandbakesbymarla

Colors
e667a6
b768aa
3276b5

Requirements
Must have
• Business Name: Treats and Bakes by Marla
• Mobile: 0427 918 053
• email: marla@treatsandbakesbymarla.com.au
• Instagram: instagram.com/treatsandbakesbymarla/
• Facebook: fb.me/treatsandbakesbymarla
Nice to have
• 2 to 3 pictures of my cakes

```html
<!DOCTYPE html>
<html lang="en">
<head>
<meta charset="utf-8">
<title>Treats and Bakes by Marla – Business Card</title>
<link rel="stylesheet" href="https://fonts.googleapis.com/css2?family=Open+Sans:wght@400;600;700&display=swap">
<style>
  :root {
    --pink: #e667a6;
    --pink-deep: #c9508c;
    --orchid: #b768aa;
    --blue: #3276b5;
    --ink: #555a60;
    --card-white: #ffffff;
    --stage: #eeeae6;
  }
  * { box-sizing: border-box; margin: 0; padding: 0; }
  html, body {
    width: 1200px;
    height: 843px;
    overflow: hidden;
  }
  body {
    background: var(--stage);
    font-family: "Open Sans", sans-serif;
    display: flex;
    align-items: center;
    justify-content: center;
    gap: 40px;
  }
  .card {
    width: 540px;
    height: 309px;
    border-radius: 4px;
    position: relative;
    overflow: hidden;
    box-shadow: 0 6px 18px rgba(0,0,0,0.15);
  }

  /* Back of card */
  .card--back {
    background: linear-gradient(100deg, var(--pink) 0%, #e873b0 45%, var(--pink-deep) 100%);
    display: flex;
    align-items: center;
    justify-content: center;
  }
  .brand-mark {
    display: flex;
    align-items: center;
    gap: 12px;
  }
  .brand-mark__dot {
    width: 18px;
    height: 18px;
    border-radius: 50%;
    flex: none;
  }
  .brand-mark__name {
    font-weight: 600;
    font-size: 27px;
    line-height: 1.15;
    text-align: center;
  }
  .card--back .brand-mark__dot { background: #ffffff; }
  .card--back .brand-mark__name { color: #ffffff; }

  /* Front of card */
  .card--front { background: var(--card-white); }
  .emblem-watermark {
    position: absolute;
    left: 70px;
    top: -10px;
    width: 170px;
    height: 300px;
    border-radius: 20px;
    background: linear-gradient(180deg, rgba(50,118,181,0.08), rgba(230,103,166,0.10));
  }
  .front-brand {
    position: absolute;
    right: 34px;
    top: 92px;
    width: 200px;
  }
  .card--front .brand-mark__dot { background: var(--pink); }
  .card--front .brand-mark__name { color: var(--pink); font-size: 23px; }

  .holder {
    position: absolute;
    left: 40px;
    top: 108px;
  }
  .holder__name {
    color: var(--pink);
    font-weight: 700;
    font-size: 17px;
    letter-spacing: 0.5px;
    text-transform: uppercase;
  }
  .holder__role {
    color: var(--ink);
    font-size: 12px;
    margin-top: 2px;
  }
  .socials {
    list-style: none;
    margin-top: 14px;
  }
  .socials li {
    display: flex;
    align-items: center;
    gap: 7px;
    color: var(--ink);
    font-size: 12px;
    line-height: 18px;
  }
  .socials__square {
    width: 10px;
    height: 10px;
    background: var(--pink);
    border-radius: 2px;
    flex: none;
  }
  .contact {
    position: absolute;
    left: 218px;
    top: 212px;
    color: var(--ink);
    font-size: 12px;
    line-height: 20px;
  }
  .contact__label { font-weight: 600; margin-right: 4px; }
  .rule {
    position: absolute;
    left: 40px;
    right: 34px;
    bottom: 34px;
    height: 1px;
    background: var(--pink);
  }
</style>
</head>
<body>
  <section class="card card--back" aria-label="Business card back">
    <div class="brand-mark">
      <span class="brand-mark__dot"></span>
      <span class="brand-mark__name">Treats and Bakes<br>by Marla</span>
    </div>
  </section>

  <section class="card card--front" aria-label="Business card front">
    <div class="emblem-watermark" role="img" aria-label="Faint brand emblem decoration"></div>

    <div class="front-brand brand-mark">
      <span class="brand-mark__dot"></span>
      <span class="brand-mark__name">Treats and Bakes<br>by Marla</span>
    </div>

    <div class="holder">
      <p class="holder__name">Dana Whitfield</p>
      <p class="holder__role">CEO/Founder</p>
      <ul class="socials">
        <li><span class="socials__square"></span>treatsandbakesbymarla</li>
        <li><span class="socials__square"></span>treatsandbakesbymarla</li>
      </ul>
    </div>

    <div class="contact">
      <p><span class="contact__label">M :</span>0427 918 053</p>
      <p><span class="contact__label">E:</span>marla@treatsandbakesbymarla.com.au</p>
    </div>

    <div class="rule"></div>
  </section>
</body>
</html>
```